依頼詳細
お悔みに掲載された方に郵送するダイレクトメールのデザインをお願いしたいと思います。すでにホームページはありますので素材はそちらをいったん利用してもらいたいと思います。
また、レイアウトなどは添付しましたエクセルに記載しています。またスキャンした現在のダイレクトメールが入っています。
記載項目
社名/フリーダイヤル/URL/キャッチコピー/
ロゴなどは現在取り寄せ中。ホームページがあるのでそこから素材をとってください。
サイズ
A4
ページ数
両面
希望イメージ
シンプル 複雑
単色 カラフル
暗い 明るい
日常 高級
遊び心 厳粛
未来的 伝統的
女性的 男性的
希望する色
緑系、グレー系
納品ファイル
• イラストレーター形式 (.ai)
• フォトショップ形式 (.psd)
補足説明
上記のファイルのいずれか。アウトラインのあり・なしのデータをお願いします。
■ 選んだ理由

クライアントの希望にあうデザインだったためです。

■ 提案者全員のお礼・コメント

たくさんのご提案ありがとうございました。またDMやパンフレットなどのデザインコンペなど行った際には、ご参加いただければ幸いです。

宜しくお願い致します。

```html
<!DOCTYPE html>
<html lang="ja">
<head>
<meta charset="utf-8">
<title>相続税や名義変更手続きに関する大切なお知らせ</title>
<link href="https://fonts.googleapis.com/css2?family=M+PLUS+Rounded+1c:wght@500;800&family=Noto+Sans+JP:wght@400;700;900&display=swap" rel="stylesheet">
<style>
:root{
  --green:#3fae2a;
  --green-dark:#1f7f1c;
  --green-light:#8fd36a;
  --green-pale:#eaf6df;
  --ink:#333;
  --white:#fff;
  --red:#e8421f;
}
*{box-sizing:border-box;margin:0;padding:0}
html,body{width:849px;height:1200px;overflow:hidden}
body{font-family:"Noto Sans JP",sans-serif;color:var(--ink);background:var(--white)}
.sheet{position:relative;width:849px;height:1200px;overflow:hidden;
  background:linear-gradient(180deg,var(--green) 0,var(--green-light) 180px,var(--green-pale) 390px,var(--green) 425px,var(--green) 795px,var(--white) 795px)}
.abs{position:absolute}
.title{left:28px;top:20px;font-family:"M PLUS Rounded 1c",sans-serif;font-weight:800;color:var(--white);font-size:47px;line-height:66px;text-shadow:0 2px 0 var(--green-dark)}
.title span{display:inline-block;background:var(--white);color:var(--green-dark);padding:0 14px;border-radius:10px;text-shadow:none}
.couple{left:640px;top:0;width:209px;height:180px;border-radius:0 0 0 90px;background:radial-gradient(circle at 60% 55%,#f3e3cf,#c9b79c 55%,var(--green-light))}
.increase{left:28px;top:205px;width:235px;height:180px;border-radius:90px;background:var(--green);border:4px solid var(--white);color:var(--white);font-weight:900;font-size:27px;line-height:42px;box-shadow:0 3px 8px rgba(0,0,0,.2);display:flex;flex-direction:column;align-items:center;justify-content:center;text-align:center}
.increase em{font-style:normal;color:#fff36b;font-size:33px}
.greeting{left:290px;top:205px;width:535px;font-size:13px;line-height:22px}
.greeting p+p{margin-top:10px}
.question{left:185px;top:415px;width:520px;height:50px;background:var(--white);border-radius:25px;text-align:center;font-weight:900;font-size:24px;line-height:50px;color:var(--green-dark)}
.checks{left:28px;top:480px;width:565px;list-style:none}
.checks li{height:48px;margin-bottom:12px;background:var(--white);border-radius:6px;display:flex;align-items:center;font-weight:700;font-size:22px;padding-left:12px;gap:12px}
.checks svg{flex:none}
.person-a{left:605px;top:478px;width:195px;height:150px;border-radius:8px;background:linear-gradient(160deg,#f5e6da,#d9bfae)}
.person-b{left:615px;top:630px;width:215px;height:155px;border-radius:8px;background:linear-gradient(160deg,#e9ded6,#b6a597)}
.advice{left:30px;top:810px;width:560px;font-size:14px;line-height:25px}
.advice p+p{margin-top:8px}
.advisor{left:605px;top:808px;width:220px;height:140px;border-radius:6px;background:linear-gradient(160deg,#e8e8e8,#9fa6ae)}
.reserve{left:180px;top:950px;font-family:"M PLUS Rounded 1c",sans-serif;font-weight:800;font-size:27px;color:var(--green);letter-spacing:4px}
.url{left:440px;top:992px;font-size:15px;display:flex;align-items:center;gap:6px}
.company{left:14px;top:990px;width:420px}
.company .since{font-size:14px;font-weight:700;line-height:20px}
.company .name{font-size:31px;font-weight:900;color:var(--green-dark);line-height:42px}
.phone{display:flex;align-items:center;gap:8px;font-size:52px;font-weight:900;color:var(--green-dark);line-height:62px;letter-spacing:-1px}
.company .addr{font-size:12.5px;line-height:22px}
.hours{display:flex;align-items:center;gap:8px;font-size:26px;font-weight:900;color:var(--green-dark);line-height:36px}
.hours small{font-size:11px;background:var(--green);color:var(--white);padding:2px 5px;border-radius:3px;font-weight:700;line-height:14px}
.hours .note{font-size:13px;font-weight:400;color:var(--ink)}
.ticket{left:440px;top:1022px;width:393px;height:150px;border:3px dashed var(--green);border-radius:8px;background:var(--white);padding:12px 14px}
.ticket .head{background:var(--green);color:var(--white);font-weight:900;font-size:24px;text-align:center;border-radius:6px;line-height:42px}
.ticket .tname{font-size:20px;font-weight:900;color:var(--green-dark);margin-top:12px}
.ticket .tphone{font-size:17px;font-weight:700}
</style>
</head>
<body>
<div class="sheet">
  <h1 class="abs title"><span>相続税や名義変更手続きに</span><br>関する大切なお知らせ</h1>
  <div class="abs couple" role="img" aria-label="年配の夫婦のイラスト"></div>

  <div class="abs increase"><span>平成27年より</span><span>相続税が<em>増税</em></span><span>されました</span></div>

  <div class="abs greeting">
    <p>このたびはご親族様の訃報、心よりお悔やみ申し上げます。突然のご不幸の中、様々な手続きに追われていらっしゃることと存じます。</p>
    <p>相続税の基礎控除が引き下げられ、これまで対象外だったご家庭でも申告が必要となる場合があります。</p>
    <p>相続・名義変更などでお困りではございませんか?一度お気軽にご相談ください。</p>
  </div>

  <div class="abs question">このようなことでお悩みではありませんか?</div>
  <ul class="abs checks">
    <li><svg width="24" height="24" viewBox="0 0 24 24"><rect x="1" y="1" width="22" height="22" rx="3" fill="none" stroke="#3fae2a" stroke-width="2"/><path d="M5 12l5 5 10-12" fill="none" stroke="#e8421f" stroke-width="3.5" stroke-linecap="round" stroke-linejoin="round"/></svg>周りに相談する人がいない</li>
    <li><svg width="24" height="24" viewBox="0 0 24 24"><rect x="1" y="1" width="22" height="22" rx="3" fill="none" stroke="#3fae2a" stroke-width="2"/><path d="M5 12l5 5 10-12" fill="none" stroke="#e8421f" stroke-width="3.5" stroke-linecap="round" stroke-linejoin="round"/></svg>相続税がかかるかの判断だけでもしてほしい</li>
    <li><svg width="24" height="24" viewBox="0 0 24 24"><rect x="1" y="1" width="22" height="22" rx="3" fill="none" stroke="#3fae2a" stroke-width="2"/><path d="M5 12l5 5 10-12" fill="none" stroke="#e8421f" stroke-width="3.5" stroke-linecap="round" stroke-linejoin="round"/></svg>相続は初めてで何をしたらよいかわからない</li>
    <li><svg width="24" height="24" viewBox="0 0 24 24"><rect x="1" y="1" width="22" height="22" rx="3" fill="none" stroke="#3fae2a" stroke-width="2"/><path d="M5 12l5 5 10-12" fill="none" stroke="#e8421f" stroke-width="3.5" stroke-linecap="round" stroke-linejoin="round"/></svg>自分で手続きをするのが不安だ</li>
    <li><svg width="24" height="24" viewBox="0 0 24 24"><rect x="1" y="1" width="22" height="22" rx="3" fill="none" stroke="#3fae2a" stroke-width="2"/><path d="M5 12l5 5 10-12" fill="none" stroke="#e8421f" stroke-width="3.5" stroke-linecap="round" stroke-linejoin="round"/></svg>役所のあいている平日になかなか休めない</li>
  </ul>
  <div class="abs person-a" role="img" aria-label="悩む女性の写真"></div>
  <div class="abs person-b" role="img" aria-label="悩む男性の写真"></div>

  <div class="abs advice">
    <p>ご遺族様の不安やお悩みをお聞かせください。<br>経験豊富な税理士や行政書士・司法書士がご相談にのります。</p>
    <p>あなたのケースに合わせてサポートいたします。<br>複雑な問題もそれぞれの専門家と解決いたします。<br>まずはお気軽に一度お近くの窓口にご相談ください。</p>
  </div>
  <div class="abs advisor" role="img" aria-label="相談員の男性の写真"></div>

  <div class="abs reserve">ご予約はこちらから</div>
  <div class="abs url"><svg width="16" height="16" viewBox="0 0 16 16"><circle cx="8" cy="8" r="7" fill="none" stroke="#3fae2a" stroke-width="1.6"/><path d="M1 8h14M8 1c3 3 3 11 0 14M8 1c-3 3-3 11 0 14" fill="none" stroke="#3fae2a" stroke-width="1.2"/></svg>http://www.midorikawa-souzoku.example</div>

  <div class="abs company">
    <div class="since">緑川で創業40年!</div>
    <div class="name">緑川相続サポートセンター</div>
    <div class="phone"><svg width="46" height="46" viewBox="0 0 24 24"><rect width="24" height="24" rx="5" fill="#1f7f1c"/><path d="M7 5l3 0 1 4-2 1c1 2 3 4 5 5l1-2 4 1 0 3c-7 1-13-5-12-12z" fill="#fff"/></svg>0120-468-157</div>
    <div class="addr">〒950-0000 新潟県緑川市本町3丁目8-14</div>
    <div class="hours"><small>受付<br>時間</small>8:00〜19:00 <span class="note">土日祝日も受付</span></div>
  </div>

  <div class="abs ticket">
    <div class="head">相談無料チケット</div>
    <div class="tname">緑川相続サポートセンター</div>
    <div class="tphone">0120-468-157 ご持参で初回相談無料</div>
  </div>
</div>
</body>
</html>
```